Business Card Design Project

We need a Business Card for an Mechanical Engineering firm in Singapore. The design should be Modern & Technical looking, yet eye catching.

Our company deals in Cutting Tools & Machine Accessories for the Manufacturing Industries such as Oil & Gas, Aero Space, etc... For more information on our Company, you can either email me or view our website www.valtrion.com.sg.

We are trying to revamp our image to give our consumers a fresh new perspective to our company, so we welcome all ideas.

Industry/Entity Type

Business

Requirements
Must have
• Must incorporate New Company Logo into the card as shown in Uploaded file.

```html
<!DOCTYPE html>
<html lang="en">
<head>
<meta charset="utf-8">
<title>Valtrion Tools – Business Card</title>
<link rel="stylesheet" href="https://fonts.googleapis.com/css2?family=Crimson+Text&family=Pathway+Gothic+One&display=swap">
<style>
  :root {
    --paper: #ffffff;
    --maroon: #8c0c34;
    --ink: #1e1e1e;
    --divider: #2b0d1f;
    --brand: #2f0f23;
  }
  * { margin: 0; padding: 0; box-sizing: border-box; }
  html, body {
    width: 1200px;
    height: 697px;
    overflow: hidden;
    background: var(--paper);
  }
  .card {
    position: relative;
    width: 1200px;
    height: 697px;
    background: var(--paper);
  }
  .contact {
    position: absolute;
    right: 680px;
    top: 182px;
    text-align: right;
  }
  .contact__name {
    font-family: "Crimson Text", Georgia, serif;
    font-weight: 400;
    font-size: 72px;
    line-height: 1;
    color: var(--maroon);
    letter-spacing: 0.5px;
    margin-bottom: 8px;
  }
  .contact__line {
    font-family: "Pathway Gothic One", "Arial Narrow", sans-serif;
    font-size: 28px;
    line-height: 37px;
    color: var(--ink);
    letter-spacing: 0.3px;
  }
  .divider {
    position: absolute;
    left: 593px;
    top: 111px;
    width: 3px;
    height: 472px;
    background: var(--divider);
  }
  .brand {
    position: absolute;
    left: 650px;
    top: 370px;
    width: 450px;
    display: flex;
    align-items: center;
    justify-content: center;
    gap: 18px;
  }
  .brand__dot {
    width: 30px;
    height: 30px;
    border-radius: 50%;
    background: var(--maroon);
    flex: none;
  }
  .brand__name {
    font-family: "Pathway Gothic One", "Arial Narrow", sans-serif;
    font-size: 66px;
    line-height: 1;
    color: var(--brand);
    letter-spacing: 1px;
    white-space: nowrap;
  }
</style>
</head>
<body>
  <main class="card">
    <section class="contact">
      <h1 class="contact__name">Daniel Reyes</h1>
      <p class="contact__line">http://www.valtrion.com.sg</p>
      <p class="contact__line">info@valtrion.com.sg</p>
      <p class="contact__line">Mob: 91 90412 37268,</p>
      <p class="contact__line">Address: 48/2 Harbor Lane,</p>
      <p class="contact__line">Riverton, New York</p>
    </section>
    <div class="divider"></div>
    <section class="brand">
      <span class="brand__dot"></span>
      <span class="brand__name">VALTRION TOOLS</span>
    </section>
  </main>
</body>
</html>
```